Vantel company profile brochure

We are looking for a 2 - 4 page brochure for our company profile.
We’re Vantel, a team of town planning and traffic and transport engineering specialists located in Melbourne, Australia.
We would like a dynamic, exciting brochure that features the colours of our logo - blue, green and grey with orange as a feature colour.
The final result should convey that Vantel is:
-Reassuring and trustworthy
-Honest and direct
- Friendly and a bit kooky
-Laid-back and casual
-Fun to work with
-Highly knowledgeable within specific areas of expertise
-Polished and professional but not afraid to show a bit of personality
-Not as ‘hard edge’ as other planners or engineers
Vantel Consultants have created a business based on providing niche, expert advice across the two main areas of urban planning and traffic engineering as well as growing areas such as social and economic analysis. They are fiercely proud of the things that make them different to other firms – they take their responsibilities seriously, they are honest and up-front, they know how to work hard but also how to relax and have a laugh, and perhaps most importantly they know how to relate to people and they care about building successful relationships with their clients, colleagues and their staff. Vantel Consultants are united by our passion for shaping the city and their desire to ensure it develops sustainably.
Many similar businesses share some of these qualities, but Vantel is rare in that they deliver the whole package. This is evidenced by our ability to attract and retain high quality staff, by our long-standing client relationships and by their commitment to progressing our own company by commissioning a brochure and business card.

Target Market(s)

Vantel’s diverse client base consists of architecture practices, builders and developers, local government and the legal fraternity so these are the areas we market to.

Industry/Entity Type

Building

Requirements
Must have
• Must use our logos colours and logo.
The logo can be altered in that the type and image do not have stay exactly as it is on the JPEG - the words and image can be placed apart / together etc.
Nice to have
• We would like an image on the front cover that we can change
Page about disciplines

```html
<!DOCTYPE html>
<html lang="en">
<head>
<meta charset="utf-8">
<title>Vantel Consultants – Disciplines</title>
<link href="https://fonts.googleapis.com/css2?family=Poppins:wght@400;600&family=Archivo+Black&display=swap" rel="stylesheet">
<style>
:root{
  --paper:#ffffff;
  --ink:#1d1d1d;
  --frame:#8a8a8a;
  --leaf-light:#c9e07a;
  --leaf-mid:#7fbf3a;
  --leaf-dark:#3f8f1f;
  --sky:#4f8fd6;
  --sky-light:#cfe3f5;
  --asphalt:#3a3a3a;
  --grass:#6aa83a;
  --silver:#d6d6d6;
  --safety:#f07a1f;
}
*{margin:0;padding:0;box-sizing:border-box}
html,body{width:1200px;height:857px;overflow:hidden;background:var(--paper)}
.spread{position:relative;width:1200px;height:857px;font-family:"Poppins",Arial,sans-serif;color:var(--ink)}
.page{position:absolute;top:28px;height:801px;border:1px solid var(--frame);background:var(--paper);overflow:hidden}
.page--left{left:34px;width:567px}
.page--right{left:600px;width:566px}
.photo{position:absolute}
.photo--leaves{left:0;top:75px;width:566px;height:192px;background:linear-gradient(160deg,var(--leaf-dark) 0%,var(--leaf-mid) 35%,var(--leaf-light) 70%,#eef5c8 100%)}
.photo--pencil{left:296px;top:505px;width:271px;height:296px;background:linear-gradient(180deg,#9fb8cf 0%,#d9dde2 35%,#8c8c8c 60%,#4a4a4a 100%)}
.photo--road{left:47px;top:0;width:212px;height:204px;background:linear-gradient(180deg,var(--sky) 0%,var(--sky-light) 55%,var(--grass) 62%,var(--asphalt) 70%,#555 100%)}
.photo--cars{left:48px;top:289px;width:207px;height:93px;background:linear-gradient(180deg,#f0f0f0 0%,var(--silver) 45%,#9a9a9a 75%,#2a2a2a 100%)}
.photo--worker{left:0;top:462px;width:566px;height:339px;background:linear-gradient(90deg,var(--asphalt) 0%,#5a5a5a 12%,var(--safety) 30%,#e9e9e9 45%,var(--sky) 62%,var(--grass) 85%,#4e8f2a 100%)}
.heading{position:absolute;left:68px;top:239px;font-family:"Archivo Black",Arial,sans-serif;font-size:19px;letter-spacing:-.3px;color:var(--ink)}
.col{position:absolute;font-size:7.6px;line-height:10.2px;letter-spacing:-.05px}
.col h3{font-weight:600;font-size:8.2px;line-height:10.6px}
.col h3.group{text-decoration:underline}
.col p{margin-bottom:10px}
.col--l1{left:70px;top:279px;width:212px}
.col--l2{left:295px;top:279px;width:236px}
.col--r1{left:47px;top:212px;width:220px}
.col--r1b{left:47px;top:384px;width:220px}
.col--r2{left:279px;top:77px;width:262px}
</style>
</head>
<body>
<div class="spread">
  <section class="page page--left">
    <div class="photo photo--leaves" role="img" aria-label="Fresh green leaves with water droplets"></div>
    <h2 class="heading">DISCIPLINES</h2>
    <div class="col col--l1">
      <h3>Planning</h3>
      <p>We use our extensive knowledge and experience to help our clients successfully navigate each step of the statutory and strategic planning processes.</p>
      <h3>Permit Applications</h3>
      <p>We have obtained planning permits for our clients on a variety of residential, commercial, entertainment and industrial projects in Melbourne, regional Victoria and interstate. Our consultative approach and extensive experience allows us to identify and resolve potential issues quickly.</p>
      <h3>VCAT Advocacy</h3>
      <p>Due to our industry expertise, Vantel’s planning team are regularly appointed as VCAT advocates for private and public clients. We have acted as representatives for diverse project types at VCAT appeals, mediations, planning panels and Consumer Affairs Victoria appeals.</p>
      <h3>VCAT Expert Evidence</h3>
      <p>XXXX [hyperlink to bio’s] frequently present expert evidence before VCAT and planning panels for a range of urban planning projects. They work closely with members of the legal fraternity, private and public clients to facilitate positive outcomes by applying their specialist knowledge.</p>
      <h3 class="group">Traffic</h3>
      <p>Vantel’s traffic engineering experts assess, analyse and design road systems and traffic management plans, working closely with our planning and transport teams.</p>
      <h3>Traffic Impact Assessment</h3>
      <p>Our team’s knowledge and experience gives us the ability to efficiently and accurately develop Traffic Impact Reports to accompany planning applications. We work across residential, commercial, industrial, sports and institutional projects and have worked with private developers and local government.</p>
    </div>
    <div class="col col--l2">
      <h3>VCAT Expert Evidence</h3>
      <p>XXXX [hyperlink to bio’s] frequently present expert evidence before VCAT and planning panels for a range of traffic projects. They assist members of the legal fraternity, private and public clients to facilitate positive outcomes by applying their specialist knowledge.</p>
      <h3>Traffic System Design</h3>
      <p>We design and plan traffic facilities for private developers and government including the detailed design of traffic signal systems for urban arterial intersections. Our experience covers both the development of new systems and the design of upgrades to existing traffic system facilities.</p>
      <h3>Local Area Traffic Management</h3>
      <p>Vantel collaborates with local governments to develop traffic management plans that address traffic, safety and amenity issues for residential areas. We have worked on projects that feature highly sensitive, complex land uses such as schools, childcare centres and kindergartens.</p>
    </div>
    <div class="photo photo--pencil" role="img" aria-label="Pencil erasing a path through tangled roads, a person walking ahead"></div>
  </section>

  <section class="page page--right">
    <div class="photo photo--road" role="img" aria-label="Paint roller laying a fresh road under a blue sky"></div>
    <div class="col col--r1">
      <h3>Road Safety Audits</h3>
      <p>We plan and assess road safety for a range of private and public sector clients. Our extensive experience includes Municipal Road Safety Strategies for over 20 Victorian local councils as well as road safety audits for road works and proposed development sites.</p>
    </div>
    <div class="photo photo--cars" role="img" aria-label="Rows of white cars with one black car in front"></div>
    <div class="col col--r1b">
      <h3>Car Parking</h3>
      <p>Vantel works with private and public clients, as well as architects and civil engineers, to prepare precinct parking plans, assess parking uses for new developments as well as assist with the planning and design of at-grade and multi-storey car parks.</p>
    </div>
    <div class="col col--r2">
      <h3 class="group">Transport</h3>
      <p>Vantel’s transport planning team offers our clients high level, accurate, strategic advice, which prioritises sustainable transport including walking, cycling and public transport.</p>
      <h3>Sustainable Transport Planning</h3>
      <p>From public transport to bike-sharing, Vantel works with private and public clients to research, plan and recommend the most suitable sustainable transport solutions for the specific needs of each project. Where needed, our team seamlessly integrates with Vantel’s planning and traffic engineering teams.</p>
      <h3>Green Travel Plans</h3>
      <p>Green travel is an increasing priority in today’s world – we work with multiple stakeholders to determine the best methods to promote and achieve sustainable transport options such as walking, cycling, car-sharing and public transport for a range of organisations including schools, workplaces and new development sites.</p>
      <h3>Major Event Planning</h3>
      <p>Vantel works with major sports and entertainment event organisers to create safe and secure traffic plans that protect competitors, participants and spectators. We recognise the unique transport requirements of large-scale events and the difference that good planning makes.</p>
      <h3>Bike Planning</h3>
      <p>Melbourne is known as a “cycle city” and Vantel’s transport team designs and assesses bicycle and pedestrian facilities, often as a component of larger road safety projects. We have experience with DDA compliance and our projects consider the special needs of pedestrians.</p>
    </div>
    <div class="photo photo--worker" role="img" aria-label="Road worker in orange safety vest crouching beside a traffic cone, green field and blue sky"></div>
  </section>
</div>
</body>
</html>
```